Label Design for 2x Chutney Products

We need a label design for 2x Chutney Products.
Mellora Chutney - Red Chili
Mellora Chutney - Green Chili & Coriander
See attached pictures. This is just sample pictures so you get an impression of the product and the colors. Both labels to have as title the generic name "Mellora Chutney" and then added either Red Chili or Green Chili & Coriander. The different terms needs to be good readable and can differ in font/color/size, or in the same style if this makes more sense from design point (as I am not a designer). The labels later on need to be editable in the way that the ingredient list, nutrition list, basis company and production information can be added. If this needs to be done directly and cannot be edited later on please let know. Editable design related the additional text also would be good as the additional information need to be added in different languages (Dutch. German and perhaps French). No clue how this is to be implemented but looking forward to receive some input/solutions on this.
I already had a project to create the company logo. I consider this logo to be used as the product logo and not the company logo. A different company logo later on can be designed from new. This logo is here attached. Either to work with this logo and use it as product logo (perhaps revise the colors) and add the product description or create a new logo for the product from scratch if you feel too. The logo itself should be easily readable for the product name/description and the colors appealing to such product and of course customers.
Please contact if any clarification needed. Thanks in advance for your efforts and ideas for this project.

Industry/Entity Type

Food

Other font styles liked:
• Asian Touch

Requirements
Nice to have
• If possible "simply" editable for text fields in order to add/revise the ingredient list, nutrition list, revise to different languages.

```html
<!DOCTYPE html>
<html lang="en">
<head>
<meta charset="utf-8">
<title>Mellora Chutney – Label Set</title>
<link href="https://fonts.googleapis.com/css2?family=Montserrat:wght@300;400;500;800&display=swap" rel="stylesheet">
<style>
  :root {
    --backdrop: #d9cfbd;
    --label-black: #0b0b0b;
    --ink-white: #f2f2f2;
    --chili-red: #e0301e;
    --chili-deep: #9c1a12;
    --herb-green: #5cb531;
    --herb-deep: #2f7a1c;
  }
  * { margin: 0; padding: 0; box-sizing: border-box; }
  html, body {
    width: 1200px;
    height: 800px;
    overflow: hidden;
    background: var(--backdrop);
    font-family: "Montserrat", sans-serif;
  }
  .label-set {
    width: 1200px;
    height: 800px;
    display: flex;
    flex-direction: column;
    justify-content: center;
    gap: 40px;
    padding: 0 60px;
  }
  .label {
    position: relative;
    height: 330px;
    background: var(--label-black);
    overflow: hidden;
  }
  .label--red { --accent: var(--chili-red); --accent-deep: var(--chili-deep); }
  .label--green { --accent: var(--herb-green); --accent-deep: var(--herb-deep); }

  .brand-mark {
    position: absolute;
    left: 32px;
    top: 30px;
    display: flex;
    align-items: center;
    gap: 10px;
  }
  .brand-mark__dot {
    width: 26px;
    height: 26px;
    border-radius: 50%;
    background: var(--accent);
  }
  .brand-mark__name {
    color: var(--ink-white);
    font-weight: 400;
    font-size: 14px;
    letter-spacing: 1px;
    text-transform: uppercase;
  }

  .illustration-chili {
    position: absolute;
    left: 40px;
    top: 90px;
    width: 120px;
    height: 240px;
    background: linear-gradient(180deg, rgba(0,0,0,0) 0%, var(--accent-deep) 100%);
    opacity: 0.55;
  }
  .illustration-herb {
    position: absolute;
    right: 60px;
    top: 0;
    width: 560px;
    height: 170px;
    background: radial-gradient(ellipse at 60% 30%, var(--accent) 0%, rgba(0,0,0,0) 70%);
    opacity: 0.6;
  }

  .product-title {
    position: absolute;
    left: 230px;
    top: 120px;
    color: var(--ink-white);
  }
  .product-title__brand {
    display: block;
    font-weight: 300;
    font-size: 46px;
    letter-spacing: 12px;
    line-height: 1;
  }
  .product-title__type {
    display: block;
    font-weight: 800;
    font-size: 104px;
    letter-spacing: 4px;
    line-height: 1;
    margin-top: 6px;
  }
  .product-variant {
    position: absolute;
    left: 234px;
    top: 278px;
    color: var(--accent);
    font-weight: 500;
    font-size: 28px;
    letter-spacing: 4px;
  }
</style>
</head>
<body>
<main class="label-set">
  <section class="label label--red">
    <div class="brand-mark">
      <span class="brand-mark__dot"></span>
      <span class="brand-mark__name">Brindle Foods</span>
    </div>
    <div class="illustration-chili" role="img" aria-label="Line drawing of red chili peppers"></div>
    <div class="illustration-herb" role="img" aria-label="Line drawing of coriander leaves in red"></div>
    <h1 class="product-title">
      <span class="product-title__brand">MELLORA</span>
      <span class="product-title__type">CHUTNEY</span>
    </h1>
    <p class="product-variant">Red Chili &amp; Coriander</p>
  </section>

  <section class="label label--green">
    <div class="brand-mark">
      <span class="brand-mark__dot"></span>
      <span class="brand-mark__name">Brindle Foods</span>
    </div>
    <div class="illustration-chili" role="img" aria-label="Line drawing of green chili peppers"></div>
    <div class="illustration-herb" role="img" aria-label="Line drawing of coriander leaves in green"></div>
    <h1 class="product-title">
      <span class="product-title__brand">MELLORA</span>
      <span class="product-title__type">CHUTNEY</span>
    </h1>
    <p class="product-variant">Green Chili &amp; Coriander</p>
  </section>
</main>
</body>
</html>
```